Private law enforcement protective services needs a kick ass brochure

We need a brochure that tops the security competition. We are a Pennsylvania based company providing law enforcement officers to the private sector to take the place of regular security officers. We are peacekeepers with the powers of arrest for any major crime committed in our presence. Our customers will get so much more by using our services over regular security. All of our officers attend annual training to stay up to date and sharp in their skills. We would like to see a design that uses the colors Royal blue, black, and grays. The final design should communicate better service over regular security yet have that soft touch and caring feeling. We want to be taken serious yet not scary. We want prospective customers to say WOW... we need to use them rather than regular security guards. We also offer K-9 services. Drug searches as well as explosive searches. THIS NEEDS TO GO ON A TRI FOLD BROCHURE. I already have a website. Www.marlowridgepatrol.com

Target Market(s)

Any business or entity where security or protective services will be needed. We provide services for events like Fairs, carnivals, churches, retail stores, large events, hostile terminations, post disaster sites, overarching of work crews in hostile areas, special celebrations, parades, sporting events,

Industry/Entity Type

Security Service

Font styles to use
Sans Serif

Requirements
Must have
• We need to have a strong professional look yet not too aggressive. DO NOT CALL OUR SERVICES SECURITY !!!! We are PEACEKEEPERS. We Keep the Peace. We provide services all across the state of Pennsylvania. We are one of Pennsylvania's best kept secrets.
Nice to have
• Pictures of Police cars, Officers on patrol at an event,

```html
<!DOCTYPE html>
<html lang="en">
<head>
<meta charset="utf-8">
<title>Marlow Ridge Patrol – Tri-fold Brochure</title>
<link href="https://fonts.googleapis.com/css2?family=Montserrat:wght@400;600;700;800&family=Open+Sans:wght@400;600&display=swap" rel="stylesheet">
<style>
  :root{
    --royal:#2c2f86;
    --royal-deep:#1d1f5e;
    --ink:#16161c;
    --charcoal:#2a2a31;
    --steel:#6d7079;
    --mist:#e9e9ea;
    --paper:#ffffff;
    --gold:#c9a24a;
    --body:#4a4c55;
  }
  *{box-sizing:border-box;margin:0;padding:0}
  html,body{width:1200px;height:2396px;overflow:hidden}
  body{background:var(--mist);position:relative;font-family:"Open Sans",Arial,sans-serif;color:var(--body)}
  .panel{position:absolute;width:366px;height:760px;overflow:hidden;box-shadow:0 6px 18px rgba(0,0,0,.18)}
  .spread{position:absolute;left:50px;width:1100px;height:760px}
  .spread .panel{top:0}
  .p1{left:0}.p2{left:367px}.p3{left:734px}

  .photo{position:absolute;left:0;width:100%}
  .brand{display:flex;align-items:center;gap:10px;font-family:"Montserrat",Arial,sans-serif;font-weight:800;color:var(--paper);font-size:20px;letter-spacing:1px;line-height:1.1}
  .brand .mark{width:34px;height:34px;border-radius:50%;background:var(--royal);flex:none}
  .brand.on-royal .mark{background:var(--gold)}

  /* cover */
  .cover{background:var(--royal)}
  .cover .photo{top:0;height:500px;background:linear-gradient(160deg,#8f949f 0%,#4b4f5c 38%,#1e2233 72%,#11131e 100%)}
  .cover svg.slant{position:absolute;left:0;top:400px}
  .cover .brand{position:absolute;left:30px;top:440px}
  .cover .tagline{position:absolute;right:28px;top:560px;text-align:right;font-family:"Montserrat",Arial,sans-serif;font-weight:800;font-size:40px;line-height:1.05;color:var(--paper)}
  .cover .url{position:absolute;left:0;right:0;bottom:18px;text-align:center;font-size:11px;color:#cfd2ea;letter-spacing:.5px}

  /* white text panels */
  .light{background:var(--paper);padding:0 26px}
  .light h2{font-family:"Montserrat",Arial,sans-serif;font-weight:800;color:var(--royal);font-size:19px;letter-spacing:.5px;margin-bottom:10px}
  .light p{font-size:10.5px;line-height:1.6;margin-bottom:12px}
  .callout{background:var(--royal);color:var(--paper);padding:14px 16px;font-size:10.5px;line-height:1.55;margin:4px 0 14px;font-weight:600}
  .foot-band{position:absolute;left:0;bottom:0;width:100%;height:22px;background:var(--royal);border-top:3px solid var(--gold)}
  .checks{list-style:none}
  .checks li{display:flex;gap:8px;font-size:10.5px;line-height:1.5;margin-bottom:7px}
  .checks svg{flex:none;margin-top:2px}

  /* dark contact panel */
  .dark{background:linear-gradient(180deg,#2b2c34 0%,var(--ink) 100%);color:#d8d9de;text-align:center;padding:60px 30px 0}
  .dark .brand{justify-content:center;margin-bottom:26px}
  .dark p{font-size:10.5px;line-height:1.65;margin-bottom:22px}
  .btn{display:inline-block;background:var(--royal);color:var(--paper);font-family:"Montserrat",Arial,sans-serif;font-weight:700;font-size:13px;letter-spacing:1px;padding:10px 26px;margin-bottom:20px}
  .contact{list-style:none;font-size:11px;line-height:2}
  .contact li{display:flex;align-items:center;justify-content:center;gap:8px}

  /* services spread */
  .services{position:absolute;left:367px;top:0;width:733px;height:760px;overflow:hidden;background:var(--ink);box-shadow:0 6px 18px rgba(0,0,0,.18)}
  .services .photo{top:0;height:100%;background:radial-gradient(ellipse at 60% 30%,#5b5e66 0%,#34363d 40%,#16171c 80%)}
  .services .brand{position:absolute;right:34px;top:50px}
  .services h2{position:absolute;left:30px;top:240px;font-family:"Montserrat",Arial,sans-serif;font-weight:800;color:var(--paper);font-size:24px;letter-spacing:.5px}
  .services h2::after{content:"";display:block;width:54px;height:3px;background:var(--gold);margin-top:8px}
  .service-list{position:absolute;left:30px;top:300px;width:620px;list-style:none;display:grid;grid-template-columns:1fr 1fr;gap:22px 30px}
  .service-list li{display:flex;gap:12px;color:#d8d9de;font-size:10.5px;line-height:1.55}
  .service-list .dot{flex:none;width:34px;height:34px;border-radius:50%;background:var(--royal);border:2px solid var(--gold)}
  .service-list b{display:block;font-family:"Montserrat",Arial,sans-serif;color:var(--paper);font-size:12px;margin-bottom:2px}
  .services svg.slant{position:absolute;left:0;bottom:0}
</style>
</head>
<body>

<!-- Front cover -->
<section class="panel cover" style="left:417px;top:29px">
  <div class="photo" role="img" aria-label="Officer in dark uniform standing at a doorway"></div>
  <svg class="slant" width="366" height="360" viewBox="0 0 366 360"><polygon points="0,70 366,0 366,360 0,360" fill="#2c2f86"/><polygon points="0,70 366,0 366,6 0,76" fill="#c9a24a"/></svg>
  <div class="brand on-royal"><span class="mark"></span>MARLOW RIDGE<br>PATROL</div>
  <div class="tagline">WE KEEP<br>THE PEACE</div>
  <div class="url">Www.marlowridgepatrol.com</div>
</section>

<!-- Outer spread -->
<div class="spread" style="top:818px">
  <section class="panel light p1">
    <div class="photo" style="top:0;height:220px;background:linear-gradient(135deg,#3a3c46,#15161b)" role="img" aria-label="Officer's peaked cap resting on a desk"></div>
    <div style="padding-top:244px">
      <h2>WHO WE ARE</h2>
      <p>Marlow Ridge Patrol places sworn peacekeepers with full powers of arrest at your business, event or site, giving you far more than a regular guard can.</p>
      <div class="callout">Serving communities across Pennsylvania with trained, caring officers who keep the peace.</div>
      <p>Every officer completes annual training to stay sharp, current and ready. We stay calm, approachable and professional so your guests feel safe, not watched.</p>
    </div>
    <div class="foot-band"></div>
  </section>

  <section class="panel dark p2">
    <div class="brand"><span class="mark"></span>MARLOW RIDGE<br>PATROL</div>
    <p>Pennsylvania's best kept secret. Real law enforcement officers for fairs, churches, retail stores, parades, sporting events and every place that needs a steady presence.</p>
    <span class="btn">CONTACT US</span>
    <ul class="contact">
      <li><svg width="12" height="12" viewBox="0 0 24 24"><path d="M6.6 10.8a15 15 0 006.6 6.6l2.2-2.2a1 1 0 011-.2 11 11 0 003.5.6 1 1 0 011 1V20a1 1 0 01-1 1A17 17 0 013 4a1 1 0 011-1h3.5a1 1 0 011 1 11 11 0 00.6 3.5 1 1 0 01-.2 1z" fill="#c9a24a"/></svg>(717) 555-0148</li>
      <li><svg width="12" height="12" viewBox="0 0 24 24"><path d="M3 5h18v14H3z M3 5l9 7 9-7" fill="none" stroke="#c9a24a" stroke-width="2"/></svg>info@marlowridgepatrol.com</li>
      <li><svg width="12" height="12" viewBox="0 0 24 24"><circle cx="12" cy="12" r="9" fill="none" stroke="#c9a24a" stroke-width="2"/><path d="M3 12h18M12 3c3 3 3 15 0 18M12 3c-3 3-3 15 0 18" fill="none" stroke="#c9a24a" stroke-width="1.5"/></svg>Www.marlowridgepatrol.com</li>
    </ul>
  </section>

  <section class="panel cover p3">
    <div class="photo" role="img" aria-label="Officer in dark uniform standing at a doorway"></div>
    <svg class="slant" width="366" height="360" viewBox="0 0 366 360"><polygon points="0,70 366,0 366,360 0,360" fill="#2c2f86"/><polygon points="0,70 366,0 366,6 0,76" fill="#c9a24a"/></svg>
    <div class="brand on-royal"><span class="mark"></span>MARLOW RIDGE<br>PATROL</div>
    <div class="tagline">WE KEEP<br>THE PEACE</div>
    <div class="url">Www.marlowridgepatrol.com</div>
  </section>
</div>

<!-- Inner spread -->
<div class="spread" style="top:1607px">
  <section class="panel light p1">
    <div style="padding-top:44px">
      <h2>WE ARE PEACEKEEPERS</h2>
      <p>We are not a security company. Our sworn officers hold the power of arrest for any major crime committed in their presence, and bring a caring, steady hand to every post.</p>
      <h2 style="margin-top:18px">WHY CHOOSE US</h2>
      <ul class="checks">
        <li><svg width="12" height="12" viewBox="0 0 24 24"><path d="M4 12l5 5L20 6" fill="none" stroke="#2c2f86" stroke-width="3"/></svg>Sworn officers with arrest powers</li>
        <li><svg width="12" height="12" viewBox="0 0 24 24"><path d="M4 12l5 5L20 6" fill="none" stroke="#2c2f86" stroke-width="3"/></svg>Annual training for every officer</li>
        <li><svg width="12" height="12" viewBox="0 0 24 24"><path d="M4 12l5 5L20 6" fill="none" stroke="#2c2f86" stroke-width="3"/></svg>Service across all of Pennsylvania</li>
        <li><svg width="12" height="12" viewBox="0 0 24 24"><path d="M4 12l5 5L20 6" fill="none" stroke="#2c2f86" stroke-width="3"/></svg>Calm, friendly and professional</li>
      </ul>
    </div>
    <div class="photo" style="bottom:22px;height:210px;background:linear-gradient(180deg,#9aa2b0,#4c5360 60%,#2a2d35)" role="img" aria-label="Patrol car parked outside a brick building"></div>
    <div class="foot-band"></div>
  </section>

  <section class="services">
    <div class="photo" role="img" aria-label="Officer's duty belt and holster in low light"></div>
    <div class="brand"><span class="mark"></span>MARLOW RIDGE<br>PATROL</div>
    <h2>OUR SERVICES</h2>
    <ul class="service-list">
      <li><span class="dot"></span><div><b>Events &amp; Festivals</b>Fairs, carnivals, parades and celebrations.</div></li>
      <li><span class="dot"></span><div><b>K-9 Searches</b>Drug and explosive detection teams.</div></li>
      <li><span class="dot"></span><div><b>Retail &amp; Churches</b>A steady, welcoming officer on site.</div></li>
      <li><span class="dot"></span><div><b>Hostile Terminations</b>Calm support during difficult moments.</div></li>
      <li><span class="dot"></span><div><b>Disaster Sites</b>Order and protection after the storm.</div></li>
      <li><span class="dot"></span><div><b>Work Crews</b>Overwatch for crews in hostile areas.</div></li>
    </ul>
    <svg class="slant" width="733" height="110" viewBox="0 0 733 110"><polygon points="0,60 733,0 733,110 0,110" fill="#2c2f86"/><polygon points="0,60 733,0 733,5 0,65" fill="#c9a24a"/></svg>
  </section>
</div>

</body>
</html>
```